Need a New "Register to Download" Graphic

You're the artist! Please get creative and if you think you can make something look better for our front page do so, get our attention and make us pick you!

Currently we have a "Buy Now" button on our website and we want to change this to say "Register to Download" the image must be the same size as the current attached button and be in the form of .png

Do not put any CoinDrift or credit card info on the image

On the current image where the CoinDrift info is wwritten replace it with "Registration Only Takes 2 Minutes!"

For extra points and to get select you can also change the box graphic on the back and make the "Get Instant Access" look better.

See current graphics http://www.plumvortex.example
Updates

Just made a guarantee on payment, thanks guys! Still waiting for more designs before we choose.

Target Market(s)

Men 18 - 26

Industry/Entity Type

Credit Card

Font styles to use
Sans Serif

Requirements
Must have
• Must blend with website

```html
<!DOCTYPE html>
<html lang="en">
<head>
<meta charset="utf-8">
<title>Register to Download Button</title>
<link rel="stylesheet" href="https://fonts.googleapis.com/css2?family=Montserrat:wght@600;700&display=swap">
<style>
  :root {
    --canvas-bg: #ffffff;
    --btn-top: #e9523f;
    --btn-mid: #d6373a;
    --btn-low: #c31f31;
    --btn-bottom: #bd1c2e;
    --shadow: #a7a7a7;
    --text-light: #ffffff;
    --icon-dark: #1b1b1b;
    --icon-ring: #c9c9c9;
  }
  html, body {
    margin: 0;
    padding: 0;
    width: 1200px;
    height: 1200px;
    overflow: hidden;
    background: var(--canvas-bg);
  }
  .canvas {
    position: relative;
    width: 1200px;
    height: 1200px;
  }
  .download-button {
    position: absolute;
    left: 214px;
    top: 403px;
    width: 752px;
    height: 164px;
  }
  .download-button svg {
    position: absolute;
    left: 0;
    top: 0;
  }
  .button-title {
    font-family: "Montserrat", sans-serif;
    font-weight: 700;
    font-size: 43px;
    fill: var(--text-light);
  }
  .button-subtitle {
    font-family: "Montserrat", sans-serif;
    font-weight: 600;
    font-size: 24px;
    fill: var(--text-light);
  }
</style>
</head>
<body>
<main class="canvas">
  <a class="download-button" aria-label="Register to download">
    <svg width="752" height="164" viewBox="0 0 752 164">
      <defs>
        <linearGradient id="button-face" x1="0" y1="0" x2="0" y2="1">
          <stop offset="0" stop-color="var(--btn-top)"/>
          <stop offset="0.5" stop-color="var(--btn-mid)"/>
          <stop offset="0.5" stop-color="var(--btn-low)"/>
          <stop offset="1" stop-color="var(--btn-bottom)"/>
        </linearGradient>
        <radialGradient id="icon-face" cx="0.4" cy="0.3" r="0.8">
          <stop offset="0" stop-color="#3a3a3a"/>
          <stop offset="1" stop-color="var(--icon-dark)"/>
        </radialGradient>
        <linearGradient id="button-shadow" x1="0" y1="0" x2="1" y2="0">
          <stop offset="0" stop-color="var(--shadow)" stop-opacity="0"/>
          <stop offset="0.1" stop-color="var(--shadow)"/>
          <stop offset="0.9" stop-color="var(--shadow)"/>
          <stop offset="1" stop-color="var(--shadow)" stop-opacity="0"/>
        </linearGradient>
      </defs>
      <ellipse class="button-shadow" cx="370" cy="158" rx="378" ry="4" fill="url(#button-shadow)"/>
      <rect class="button-face" x="8" y="0" width="734" height="156" rx="26" fill="url(#button-face)"/>
      <text class="button-title" x="49" y="67" textLength="551" lengthAdjust="spacingAndGlyphs">REGISTER TO DOWNLOAD</text>
      <text class="button-subtitle" x="102" y="120" textLength="426" lengthAdjust="spacingAndGlyphs">Registration takes only 2 minutes</text>
      <g class="download-icon" aria-hidden="true">
        <circle cx="664" cy="78" r="50" fill="var(--icon-ring)"/>
        <circle cx="664" cy="78" r="46" fill="url(#icon-face)"/>
        <polygon points="646,66 682,66 664,100" fill="var(--text-light)"/>
      </g>
    </svg>
  </a>
</main>
</body>
</html>
```